Where Did the River Turn: A Season of Mending

The book size is 6x9. I am more interested in an illustrative design like the one I have posted below with a picture of my face and then having elements in the background of a barn, a cross and my little girls eyes peaking out from behind the scenery.
"Where Did the River Turn… A Season of Mending" is a gripping memoir of resilience, faith, and courage. Lorelle Brantmoor’s journey pulls back the curtain on a ranch family fractured by addiction, abuse, and chaos, while revealing an extraordinary path to self-discovery and purpose.
Lorelle, her older sister Kimbra, and their three younger brothers grow up in a destabilizing environment where frequent moves and changing schools are routine. All the while, they navigate life in the shadow of their father’s addiction, schizophrenia, and violent outbursts. With dark secrets of sexual abuse and domestic violence lurking behind closed doors, the family seems trapped in a cycle of destruction.
Yet, Lorelle’s spirit remains unbroken. Anchored by her unshakable belief that God is her true father and Jesus her brother, she clings to her faith and a guiding philosophy she calls “the next right move”—a quiet force that propels her forward, even as those around her fall victim to their demons. As her siblings descend into addiction, incarceration, and heartbreak, Lorelle works to protect herself from the same fate while holding onto the family she cherishes.
Described by those who know her as possessing sophisticated grit, Lorelle rises above her circumstances with a unique blend of resilience, conscientiousness, and inner grace. She is driven by her belief in “organic truth”—the truth you possess before you are even born—which, once discovered, has the power to set you free into becoming who you were met to be. This profound conviction, along with her commitment to “the next right move,” guides her through life’s darkest moments.
Armed with a PhD in Human Science and experience as a child abuse and neglect investigator, therapist, professor, business leader and coach, Lorelle’s true triumph lies in something far deeper: surviving three near-death experiences and realizing that her purpose transcends personal, professional, and material achievements. Rather than pursuing happiness, she dedicates herself to uncovering meaning.
In this inspiring and candid memoir, she invites readers on a journey of becoming—one marked by faith, perseverance, and the courage to listen to the voice of organic truth within. Her story is a testament to the resilience of the human spirit and a beacon of hope for anyone navigating their own path to reclaim their sense of self, purpose, and freedom.

```html
<!DOCTYPE html>
<html lang="en">
<head>
<meta charset="utf-8">
<title>Where Did the River Turn? – A Season of Mending</title>
<link rel="stylesheet" href="https://fonts.googleapis.com/css2?family=Jost:wght@400;500&display=swap">
<style>
  :root {
    --backdrop: #00453f;
    --cover-paper: #e6e6e4;
    --title-green: #00463f;
    --ink: #1f1f1f;
    --bronze: #b0855a;
    --name-white: #ffffff;
    --portrait-dark: #3a302c;
    --portrait-skin: #c9a893;
    --portrait-light: #f3f2ef;
  }
  html, body {
    margin: 0;
    padding: 0;
    width: 1200px;
    height: 1200px;
    overflow: hidden;
    background: var(--backdrop);
  }
  .book-cover {
    position: absolute;
    left: 240px;
    top: 60px;
    width: 720px;
    height: 1080px;
    background: var(--cover-paper);
    box-shadow: 6px 8px 14px rgba(0, 0, 0, 0.35);
    overflow: hidden;
    font-family: "Jost", sans-serif;
  }
  .author-portrait {
    position: absolute;
    left: 150px;
    top: 496px;
    width: 430px;
    height: 501px;
    border-radius: 140px 140px 0 0;
    background:
      radial-gradient(ellipse 38% 30% at 50% 26%, var(--portrait-skin) 0%, rgba(201,168,147,0) 100%),
      linear-gradient(180deg, var(--portrait-dark) 0%, #6e625b 38%, #d9d6d1 62%, var(--portrait-light) 100%);
    -webkit-mask-image: radial-gradient(ellipse 60% 75% at 50% 55%, #000 60%, transparent 100%);
    mask-image: radial-gradient(ellipse 60% 75% at 50% 55%, #000 60%, transparent 100%);
    opacity: 0.85;
  }
  .cover-title {
    position: absolute;
    left: 0;
    top: 44px;
    width: 100%;
    margin: 0;
    text-align: center;
    color: var(--title-green);
    font-weight: 400;
    font-size: 112px;
    line-height: 97px;
    letter-spacing: -2px;
    text-transform: uppercase;
  }
  .cover-title span { display: block; }
  .cover-subtitle {
    position: absolute;
    left: 0;
    top: 378px;
    width: 100%;
    margin: 0;
    text-align: center;
    color: var(--ink);
    font-weight: 400;
    font-size: 19px;
    letter-spacing: 3px;
  }
  .divider-rule {
    position: absolute;
    left: 0;
    top: 997px;
    width: 100%;
    height: 7px;
    background: linear-gradient(90deg, var(--title-green) 0%, var(--title-green) 35%, #c9d3d1 50%, var(--title-green) 65%, var(--title-green) 100%);
  }
  .author-band {
    position: absolute;
    left: 0;
    top: 1004px;
    width: 100%;
    height: 76px;
    background: var(--bronze);
    display: flex;
    align-items: center;
    justify-content: center;
  }
  .author-name {
    margin: 0;
    color: var(--name-white);
    font-weight: 400;
    font-size: 33px;
    letter-spacing: 1.5px;
  }
</style>
</head>
<body>
  <div class="book-cover">
    <div class="author-portrait" role="img" aria-label="Portrait photograph of the author with long dark hair in a white blazer, hands clasped, against a light grey studio backdrop"></div>
    <h1 class="cover-title">
      <span>Where Did</span>
      <span>The River</span>
      <span>Turn?</span>
    </h1>
    <p class="cover-subtitle">A Season of Mending</p>
    <div class="divider-rule"></div>
    <div class="author-band">
      <p class="author-name">Lorelle Brantmoor PHD (DR. LORE)</p>
    </div>
  </div>
</body>
</html>
```